Metal fabrication company website refresh

Our client want's a fresh look to their website
https://www.torvalinegroup.com.au/

They may use a video as their hero shot, but like product photos.

Current logo is here: https://www.torvalinegroup.com.au/wp-content/uploads/2015/05/logo.png
Current logo with slogan is here: https://www.torvalinegroup.com.au/wp-content/uploads/2023/10/torvaline_logo_with_slogan.jpg

Colors should be masculine, but they want a little more 'personal' feeling. We may be able to achieve this with photos of the staff or maybe a drone video. They like photos and sliders.

They use their certifications on their emails, and the ISO certifications are the most important so if you can find a nice way to show them but not so they stand out too much it would be nice. Their certification logos that they use in their email are here: https://www.torvalinegroup.com.au/wp-content/uploads/2023/10/torvaline_certifications.pdf

They would prefer to go to a more 'one page' approach with some secondary pages like projects, about, products linked from a home page summary

```html
<!DOCTYPE html>
<html lang="en">
<head>
<meta charset="utf-8">
<title>Torvaline — Security Fencing &amp; Metal Fabrication</title>
<link rel="stylesheet" href="https://fonts.googleapis.com/css2?family=Poppins:wght@400;500;600;700&display=swap">
<style>
:root{
  --green:#2f9422;
  --green-bright:#3aa52a;
  --black:#000;
  --ink:#111;
  --text:#333;
  --muted:#555;
  --panel:#242a30;
  --footer-bar:#f2f2f2;
  --white:#fff;
}
*{box-sizing:border-box;margin:0;padding:0}
html,body{width:1200px;height:4169px;overflow:hidden;background:var(--white);font-family:"Poppins",sans-serif;color:var(--text)}
.page{position:relative;width:1200px;height:4169px}
.abs{position:absolute}

/* header */
.site-header{position:absolute;left:0;top:0;width:1200px;height:163px;background:var(--black)}
.brand{position:absolute;left:86px;top:58px;color:var(--white);font-weight:500;font-size:34px;line-height:1;letter-spacing:.5px}
.nav a{position:absolute;top:70px;color:var(--white);font-size:15px;text-decoration:none}
.nav a.active{color:var(--green-bright)}
.nav a.active::after{content:"";position:absolute;left:0;right:0;bottom:-9px;height:2px;background:var(--green-bright)}

/* hero */
.hero-title{left:85px;top:282px;width:520px;font-size:46px;font-weight:700;line-height:1.14;color:var(--ink)}
.hero-title .accent{color:var(--green);font-size:54px}
.hero-text{left:87px;top:496px;width:460px;font-size:15px;line-height:26px;color:var(--text)}
.btn{position:absolute;display:flex;align-items:center;justify-content:center;background:var(--green);color:var(--white);text-decoration:none}
.hero-btn{left:87px;top:636px;width:172px;height:43px;font-size:15px}
.hero-video{left:610px;top:251px;width:506px;height:481px;border-radius:14px;background:linear-gradient(180deg,#9fb2c2 0%,#b66a45 40%,#a55b3c 70%,#8d8a85 100%)}
.play{left:821px;top:450px;width:84px;height:84px}

/* certifications */
.cert-arrow{width:42px;height:42px}
.cert{top:834px;width:155px;height:151px}

/* about */
.about-title{left:646px;top:1165px;font-size:62px;font-weight:500;color:var(--green)}
.about-text{left:646px;top:1270px;width:460px;font-size:15px;line-height:21.5px;color:var(--text)}
.about-text p+p{margin-top:21px}
.about-btn{left:645px;top:1532px;width:152px;height:44px;font-size:20px;font-weight:500}

/* sections */
.section-title{left:0;width:1200px;text-align:center;font-size:64px;font-weight:500;color:var(--green)}
.card{border-radius:12px}
.label{width:329px;text-align:center;font-size:20px;font-weight:600;color:#333;line-height:29px;letter-spacing:.3px}
.view-all{left:526px;top:1976px;width:146px;height:44px;border:2px solid #ddd;color:var(--white);font-size:15px;font-weight:500;display:flex;align-items:center;justify-content:center}
.panel{left:787px;top:2778px;width:329px;height:422px;background:var(--panel);color:var(--white);text-align:center}
.panel h3{margin-top:64px;font-size:26px;font-weight:600}
.panel p{margin:36px auto 0;width:290px;font-size:15px;line-height:24px}
.panel .outline{display:inline-block;margin-top:40px;padding:10px 30px;border:2px solid #ddd;font-size:14px;font-weight:500}

/* footer */
.foot-brand{left:121px;top:3898px;font-size:30px;font-weight:500;color:var(--ink)}
.foot-head{top:3830px;font-size:19px;font-weight:500;color:var(--green)}
.foot-list{list-style:none;top:3888px;font-size:21px;line-height:35px;color:#222}
.news-head{left:813px;top:3832px;font-size:17px;font-weight:500;color:var(--green)}
.news-text{left:812px;top:3870px;width:290px;font-size:15px;line-height:25px;color:#333}
.news-form{left:813px;top:3940px;width:256px;height:51px;border:2px solid var(--green);padding:3px;display:flex}
.news-form span{flex:1;font-size:15px;color:#777;display:flex;align-items:center;padding-left:8px}
.news-form b{width:100px;background:var(--green);color:var(--white);font-weight:500;font-size:16px;display:flex;align-items:center;justify-content:center}
.foot-bar{left:0;top:4069px;width:1200px;height:100px;background:var(--footer-bar)}
.copy{left:84px;top:4104px;font-size:18px;color:#222}
.social{top:4104px;width:24px;height:24px;border-radius:50%}
</style>
</head>
<body>
<div class="page">

<header class="site-header">
  <div class="brand">Torvaline</div>
  <nav class="nav">
    <a class="active" href="#" style="left:572px">Home</a>
    <a href="#" style="left:640px">About us</a>
    <a href="#" style="left:729px">services</a>
    <a href="#" style="left:811px">Our projects</a>
    <a href="#" style="left:926px">Products</a>
    <a href="#" style="left:1027px">Contact us</a>
  </nav>
</header>

<section class="hero">
  <h1 class="abs hero-title"><span class="accent">Torvaline</span> Specialise in all types of&nbsp; Care Security Fencing</h1>
  <p class="abs hero-text">We chose to re-brand as our growth in custom fabrication and projects has grown beyond our traditional perimeter products for just about any project.</p>
  <a class="btn hero-btn" href="#">Read More</a>
  <div class="abs hero-video" role="img" aria-label="Video still of a steel picket fence in front of a brick building"></div>
  <svg class="abs play" viewBox="0 0 84 84" aria-hidden="true"><circle cx="42" cy="42" r="42" fill="rgba(40,40,40,.75)"/><path d="M34 28 L58 42 L34 56 Z" fill="#fff"/></svg>
</section>

<section class="certifications" aria-label="Certifications">
  <svg class="abs cert-arrow" style="left:90px;top:884px" viewBox="0 0 42 42"><circle cx="21" cy="21" r="21" fill="var(--green)"/><path d="M24 14 L17 21 L24 28" stroke="#fff" stroke-width="4" fill="none"/></svg>
  <div class="abs cert" role="img" aria-label="ISO certification badge" style="left:167px;background:#111"></div>
  <div class="abs cert" role="img" aria-label="ISO certification badge" style="left:342px;width:149px;background:#f2c21a"></div>
  <div class="abs cert" role="img" aria-label="Accreditation badge" style="left:534px;width:130px;background:#e6ecf5"></div>
  <div class="abs cert" role="img" aria-label="ISO certification badge" style="left:701px;width:157px;background:#1f9a3c"></div>
  <div class="abs cert" role="img" aria-label="ISO certification badge" style="left:881px;width:157px;background:#e32b35"></div>
  <svg class="abs cert-arrow" style="left:1062px;top:884px" viewBox="0 0 42 42"><circle cx="21" cy="21" r="21" fill="var(--green)"/><path d="M18 14 L25 21 L18 28" stroke="#fff" stroke-width="4" fill="none"/></svg>
</section>

<section class="about">
  <div class="abs" role="img" aria-label="Louvred metal screen on the side of a building" style="left:107px;top:1153px;width:440px;height:440px;border-radius:50%;background:linear-gradient(135deg,#8a9099 0%,#c9ced4 50%,#6f757c 100%)"></div>
  <div class="abs" role="img" aria-label="Steel access ladder on a building wall" style="left:314px;top:1404px;width:220px;height:220px;border-radius:50%;border:6px solid #fff;background:linear-gradient(160deg,#d5d3cf,#a9a6a0)"></div>
  <h2 class="abs about-title">About Us</h2>
  <div class="abs about-text">
    <p>We chose to re-brand as our growth in custom fabrication and projects has grown beyond our traditional perimeter fencing products. We make custom products and can now deliver a truly comprehensive range of metal products for hope you like our new branding project.</p>
    <p>railstead.com.au emails and web address will continue to operate, but our new website and email addresses have become torvalinegroup same&nbsp; of products and customer service.</p>
  </div>
  <a class="btn about-btn" href="#">Read More</a>
</section>

<section class="products">
  <h2 class="abs section-title" style="top:1748px">Our Products</h2>
  <div class="abs card" role="img" aria-label="Automated boom gate at a site entrance" style="left:92px;top:1890px;width:329px;height:219px;background:linear-gradient(180deg,#a9c6e3 0%,#6c7d57 45%,#b43a33 65%,#c9c2b5 100%)"></div>
  <div class="abs card" role="img" aria-label="Chainwire fence at dusk" style="left:434px;top:1890px;width:329px;height:219px;background:linear-gradient(180deg,#3a3f44,#262a2e)"></div>
  <div class="abs view-all">VIEW ALL</div>
  <div class="abs card" role="img" aria-label="Metal stairs and timber-look screens" style="left:777px;top:1890px;width:329px;height:219px;background:linear-gradient(135deg,#c5cbd0,#6b5a4b 50%,#d2d6d9)"></div>
  <div class="abs label" style="left:92px;top:2129px">GATE AUTOMATION</div>
  <div class="abs label" style="left:434px;top:2129px">CHAINWIRE FENCING</div>
  <div class="abs label" style="left:777px;top:2129px">METAL WORKS</div>

  <div class="abs card" role="img" aria-label="High security gate with razor wire" style="left:92px;top:2209px;width:329px;height:219px;background:linear-gradient(180deg,#e8edf2,#4a4f53 60%,#8a8580)"></div>
  <div class="abs card" role="img" aria-label="Timber steps with hand rails down to water" style="left:434px;top:2209px;width:329px;height:219px;background:linear-gradient(180deg,#a7aab0,#6d7f5a 50%,#9a6a45)"></div>
  <div class="abs card" role="img" aria-label="Guardrail louvres on a parking structure" style="left:777px;top:2209px;width:329px;height:219px;background:linear-gradient(180deg,#dfe7ef,#5d6f7c 50%,#a8b4bc)"></div>
  <div class="abs label" style="left:92px;top:2448px">HIGH SECURITY<br>FENCING</div>
  <div class="abs label" style="left:434px;top:2448px">HAND RAILS</div>
  <div class="abs label" style="left:777px;top:2448px">GAURDRAIL AND VECHICLE<br>CONTROL SYSTEM</div>

  <svg class="abs cert-arrow" style="left:552px;top:2530px" viewBox="0 0 42 42"><circle cx="21" cy="21" r="21" fill="var(--green)"/><path d="M24 14 L17 21 L24 28" stroke="#fff" stroke-width="4" fill="none"/></svg>
  <svg class="abs cert-arrow" style="left:604px;top:2530px" viewBox="0 0 42 42"><circle cx="21" cy="21" r="21" fill="var(--green)"/><path d="M18 14 L25 21 L18 28" stroke="#fff" stroke-width="4" fill="none"/></svg>
</section>

<section class="projects">
  <h2 class="abs section-title" style="top:2640px">Our Projects</h2>
  <div class="abs" role="img" aria-label="Black palisade fence beside a car park" style="left:81px;top:2778px;width:329px;height:422px;background:linear-gradient(180deg,#8fb2d8 0%,#4d5358 45%,#bfc3c6 75%,#3d3f42)"></div>
  <div class="abs" role="img" aria-label="Louvred screens on a multi-level car park" style="left:434px;top:2778px;width:329px;height:277px;background:linear-gradient(180deg,#e4ecf4,#5e7180 55%,#a9b3ba)"></div>
  <div class="abs" role="img" aria-label="Curved guardrail and black fence by a road" style="left:434px;top:3078px;width:329px;height:278px;background:linear-gradient(180deg,#c8d6e2,#43503c 45%,#9aa0a3 75%,#4a4d50)"></div>
  <div class="abs" role="img" aria-label="Warehouse interior with steel framing" style="left:434px;top:3379px;width:329px;height:277px;background:linear-gradient(180deg,#d9dde0,#a3a8ab 60%,#7b7f82)"></div>
  <div class="abs panel">
    <h3>HIGH SECURITY</h3>
    <p>Railstead specialise in all types of high-security fencing. We are accredited and have done work for Gridmark, Eastvale Power, Transline and a host of other clients with exacting security requirements.</p>
    <span class="outline">READ MORE</span>
  </div>
  <div class="abs" role="img" aria-label="Steel access ladder on a clad wall" style="left:81px;top:3232px;width:329px;height:423px;background:linear-gradient(160deg,#d6d4d0,#aeaba6 60%,#8d8a85)"></div>
  <div class="abs" role="img" aria-label="Timber stairs with steel hand rail near water" style="left:787px;top:3232px;width:329px;height:423px;background:linear-gradient(180deg,#a5a9ae,#5e7a47 40%,#9b6b45 80%,#6d5a44)"></div>
  <svg class="abs cert-arrow" style="left:551px;top:3702px" viewBox="0 0 42 42"><circle cx="21" cy="21" r="21" fill="var(--green)"/><path d="M24 14 L17 21 L24 28" stroke="#fff" stroke-width="4" fill="none"/></svg>
  <svg class="abs cert-arrow" style="left:603px;top:3702px" viewBox="0 0 42 42"><circle cx="21" cy="21" r="21" fill="var(--green)"/><path d="M18 14 L25 21 L18 28" stroke="#fff" stroke-width="4" fill="none"/></svg>
</section>

<footer>
  <div class="abs foot-brand">Torvaline</div>
  <div class="abs foot-head" style="left:345px">QUICK LINKS</div>
  <ul class="abs foot-list" style="left:347px"><li>About</li><li>Services</li><li>Contact</li><li>Home</li></ul>
  <div class="abs foot-head" style="left:565px">INFORMATION</div>
  <ul class="abs foot-list" style="left:565px"><li>Terms &amp; Condition</li><li>Privacy Policy</li><li>About Us</li><li>Support</li></ul>
  <div class="abs news-head">NEWSLETTER</div>
  <p class="abs news-text">Join our newsletter to stay up date with our latest updates</p>
  <div class="abs news-form"><span>Enter Your Email</span><b>Sign up</b></div>
  <div class="abs foot-bar"></div>
  <div class="abs copy">All rights reserved.Copyrights @ 2023</div>
  <div class="abs social" aria-label="Social link" style="left:981px;background:#c13584"></div>
  <div class="abs social" aria-label="Social link" style="left:1018px;background:#1da1f2"></div>
  <div class="abs social" aria-label="Social link" style="left:1054px;background:#3b5998"></div>
</footer>

</div>
</body>
</html>
```